Etiketten-Design für Eierschachtel
Zielgruppe
Wir haben einen Hofladen, indem wir unsere hofeigenen Produkte direkt an den Verbraucher verkaufen.
Aufgabenstellung
Wir suchen ein Etikett für unsere Eierschachtel, die wir für den Verkauf unserer Eier im eigenen Hofladen benötigen.
Das Etikett soll hell und freundlich, aber keinesfalls überladen oder zu verspielt sein. Es soll die Natürlichkeit und Regionalität widerspiegeln. Wir halten unsere Hühner in mobiler Freilandhaltung mit ausreichend Auslauf auf unseren Wiesen.
Das beigefügte Logo (einmal farbig, einmal schwarz/weiß - je nach Vorschlag was besser passt) soll integriert werden.
Das Etikett soll folgende Punkte enthalten:
Rückseite:
- 'Verbraucherhinweis: Nach dem Kauf bei Kühlschranktemperatur aufbewahren. Nach Ablauf des
Mindesthaltbarkeitsdatums durcherhitzen.'
- Familie Lohwanger
Tannweg 27
74912 Kellinghofen
Vorderseite (zum Öffnen der Eierschachtel) bzw. Deckel oben:
- '10 frische Eier aus mobiler Freilandhaltung' (gerne auch eigene Vorschläge von Ihnen)
- passender Slogan, der auf Regionalität bzw. Einkaufen direkt beim Erzeuger basiert
Format: ca. 21,4cm breit und ca. 14,2cm lang

```html
<!DOCTYPE html>
<html lang="de">
<head>
<meta charset="utf-8">
<title>Etikett Eierschachtel – Lohwanger Hof</title>
<link rel="stylesheet" href="https://fonts.googleapis.com/css2?family=Open+Sans:wght@400;600;700&family=Signika:wght@400;600&display=swap">
<style>
  :root {
    --page: #ffffff;
    --band-green: #80b77d;
    --band-brown: #a97b52;
    --title-red: #7e3210;
    --logo-green: #3f8a3a;
    --egg: #f4f1ea;
    --text-dark: #3a2a1a;
    --text-light: #ffffff;
  }
  html, body {
    margin: 0;
    padding: 0;
    width: 1200px;
    height: 2311px;
    overflow: hidden;
    background: var(--page);
    font-family: "Open Sans", Arial, sans-serif;
  }
  .label {
    position: absolute;
    left: 257px;
    top: 972px;
    width: 686px;
    height: 366px;
    overflow: hidden;
  }
  .info-band {
    position: absolute;
    left: 0; top: 0;
    width: 100%; height: 64px;
    background: var(--band-green);
    color: var(--text-light);
  }
  .consumer-note {
    position: absolute;
    left: 39px; top: 16px;
    font-size: 7px;
    line-height: 9px;
  }
  .consumer-note .heading,
  .farm-address .heading {
    font-size: 8px;
    font-weight: 700;
    text-decoration: underline;
    margin-bottom: 2px;
  }
  .farm-address {
    position: absolute;
    left: 555px; top: 16px;
    font-size: 7px;
    line-height: 9px;
  }
  .hero {
    position: absolute;
    left: 0; top: 64px;
    width: 100%; height: 236px;
  }
  .hero-photo {
    position: absolute;
    inset: 0;
    background:
      radial-gradient(ellipse 120px 110px at 470px 120px, #a8562a 0%, #a8562a 40%, transparent 75%),
      linear-gradient(90deg, #d9d8d2 0%, #c9cbc2 25%, #9fb783 45%, #6e9c4d 65%, #4f8a38 85%, #5d963f 100%);
  }
  .brand {
    position: absolute;
    left: 42px; top: 66px;
    width: 160px;
    text-align: center;
  }
  .brand-mark {
    display: block;
    margin: 0 auto 6px;
  }
  .brand-name {
    font-family: "Open Sans", Arial, sans-serif;
    font-weight: 600;
    font-size: 17px;
    letter-spacing: 0.5px;
    color: var(--logo-green);
  }
  .title-box {
    position: absolute;
    left: 191px; top: 80px;
    width: 242px; height: 48px;
    background: var(--title-red);
    color: var(--text-light);
    padding: 3px 0 0 12px;
    box-sizing: border-box;
    font-family: "Signika", Arial, sans-serif;
  }
  .title-main {
    font-size: 27px;
    font-weight: 600;
    line-height: 27px;
  }
  .title-sub {
    font-size: 12px;
    line-height: 13px;
  }
  .egg-badge {
    position: absolute;
    left: 532px; top: 164px;
  }
  .egg-badge .count {
    font-family: "Signika", Arial, sans-serif;
    font-weight: 600;
    font-size: 30px;
    fill: var(--text-dark);
  }
  .egg-badge .count-label {
    font-size: 6.5px;
    font-weight: 700;
    fill: var(--text-dark);
  }
  .slogan-band {
    position: absolute;
    left: 0; top: 300px;
    width: 100%; height: 66px;
    background: var(--band-brown);
    color: var(--text-light);
    display: flex;
    align-items: center;
    justify-content: center;
    font-size: 17px;
  }
</style>
</head>
<body>
  <section class="label">
    <header class="info-band">
      <div class="consumer-note">
        <div class="heading">Verbraucherhinweis:</div>
        Nach dem Kauf bei Kühlschranktemperatur aufbewahren.<br>
        Nach Ablauf des Mindesthaltbarkeitsdatums durcherhitzen.
      </div>
      <div class="farm-address">
        <div class="heading">Familie Lohwanger</div>
        Tannweg 27<br>
        74912 Kellinghofen
      </div>
    </header>

    <div class="hero">
      <div class="hero-photo" role="img" aria-label="Foto: braunes Huhn auf einer sonnigen Wiese, links ein heller, unscharfer Weg"></div>

      <div class="brand">
        <svg class="brand-mark" width="64" height="64" viewBox="0 0 64 64" aria-hidden="true">
          <circle cx="32" cy="32" r="30" fill="none" stroke="var(--logo-green)" stroke-width="1.5"/>
        </svg>
        <div class="brand-name">LOHWANGER HOF</div>
      </div>

      <div class="title-box">
        <div class="title-main">FRISCHE EIER AUS</div>
        <div class="title-sub">MOBILER FREILANDHALTUNG</div>
      </div>

      <svg class="egg-badge" width="64" height="72" viewBox="0 0 64 72" aria-label="10 frische Eier">
        <path d="M32 2 C52 2 62 32 62 50 C62 66 50 74 32 74 C14 74 2 66 2 50 C2 32 12 2 32 2 Z" fill="var(--egg)"/>
        <text class="count" x="32" y="40" text-anchor="middle">10</text>
        <text class="count-label" x="32" y="52" text-anchor="middle">FRISCHE EIER</text>
      </svg>
    </div>

    <footer class="slogan-band">Weil es aus der Region am besten ist</footer>
  </section>
</body>
</html>
```